Tovane Medical Artificial Intelligence MedTech Software Website Refresh

We need a new website (old one at www.tovane-medical.example is no longer relevant) for our medtech software company using artificial intelligence to deliver higher quality, faster and more cost effective care in oncology. The audiences are both healthcare providers and health insurance payers. We've created an extensive outline to follow and have the old site still live for easy content use and repurposing. Our primary need is a great overhaul to look and feel. If we find a successful designer, we will need additional work done for graphics and other presentation projects.

Target Market(s)

Health care providers (doctors) and administrators plus health insurers

Industry/Entity Type

Medtech

Number of Pages Required

5+ page

Font styles to use
Other font styles liked:
• Roboto see Style Guide

Requirements
Must have
• See attached brief
Nice to have
• See attached brief. We like www.curaplex.example and www.lumidorhealth.example as sites.
Should not have
• See attached brief

```html
<!DOCTYPE html>
<html lang="en">
<head>
<meta charset="utf-8">
<title>Tovane Medical — Cost Effective Care in Oncology</title>
<link rel="stylesheet" href="https://fonts.googleapis.com/css2?family=Exo+2:wght@500;600;700&family=Roboto:wght@400;500;700&display=swap">
<style>
:root{
  --brand:#1b74c2;
  --brand-dark:#155fa8;
  --sky:#22a9e0;
  --sky-light:#94defe;
  --text:#1c1c1c;
  --muted:#333;
  --white:#fff;
  --field:#f1f1f1;
}
*{box-sizing:border-box;margin:0;padding:0}
html,body{width:1200px;height:3551px;overflow:hidden;background:var(--white)}
body{font-family:"Roboto",sans-serif;color:var(--text);position:relative}
.abs{position:absolute}
.heading{font-family:"Exo 2",sans-serif;font-weight:700;color:var(--brand);text-transform:uppercase;letter-spacing:.5px}
.btn{position:absolute;display:flex;align-items:center;justify-content:center;border-radius:40px;background:var(--sky);color:var(--white);font-family:"Exo 2",sans-serif;font-weight:700;font-size:15px;text-transform:uppercase;letter-spacing:.3px;text-decoration:none}

/* header */
.site-header{position:absolute;left:0;top:0;width:1200px;height:110px;background:var(--white);box-shadow:0 2px 4px rgba(0,0,0,.08);z-index:2}
.brand-name{position:absolute;font-family:"Exo 2",sans-serif;font-weight:700;color:var(--brand);line-height:1;white-space:nowrap}
.header-brand{left:172px;top:38px;font-size:32px}
.main-nav{position:absolute;left:618px;top:45px;display:flex;gap:18px;font-weight:500;font-size:15px;color:var(--text)}

/* hero */
.hero-media{position:absolute;left:0;top:110px;width:1200px;height:450px;background:linear-gradient(90deg,#fbfcfd 0%,#eef3f7 45%,#d4e2ea 70%,#b9d3dd 100%)}
.hero-title{position:absolute;left:172px;top:208px;font-size:48px;line-height:62px}

/* about & problems */
.about-title{position:absolute;left:0;width:1200px;top:650px;text-align:center;font-size:34px}
.about-text{position:absolute;left:200px;width:800px;top:704px;text-align:center;font-size:15px;line-height:26px}
.section-title{font-size:30px;white-space:nowrap}
.body-copy{font-size:14.5px;line-height:26.5px;color:var(--muted);text-align:justify}
.illus{position:absolute;border-radius:30px}
.bubble{position:absolute;border-radius:50%;background:#f1f7fc}

/* services */
.services{position:absolute;left:0;top:1637px;width:1200px;height:614px;background:var(--sky)}
.services-title{position:absolute;left:0;width:1200px;top:80px;text-align:center;color:var(--white);font-size:34px}
.service-icon{position:absolute;width:126px;height:126px;border-radius:50%;background:var(--brand-dark)}
.service-name{position:absolute;font-family:"Exo 2",sans-serif;font-weight:500;font-size:32px;color:var(--white);white-space:nowrap}
.service-copy{position:absolute;width:257px;font-size:13px;line-height:19px;color:var(--white);text-align:justify}

/* footer */
.contact-left{position:absolute;left:0;top:2770px;width:500px;height:693px;background:var(--brand)}
.contact-right{position:absolute;left:500px;top:2770px;width:700px;height:693px;background:var(--sky-light)}
.footer-brand{left:172px;top:175px;font-size:44px;color:var(--white)}
.hours-title{position:absolute;left:172px;top:305px;color:var(--white);font-size:30px}
.hours{position:absolute;left:172px;font-size:16px;color:var(--white)}
.form-title{position:absolute;left:45px;top:105px;font-size:30px;line-height:40px}
.field-label{position:absolute;font-size:14px;color:var(--text)}
.field{position:absolute;background:var(--field);border-radius:30px;border:1px solid #e2e2e2}
.copyright{position:absolute;left:0;width:1200px;top:3505px;text-align:center;font-size:13.5px;font-weight:500}
</style>
</head>
<body>

<header class="site-header">
  <div class="brand-name header-brand">Tovane Medical</div>
  <nav class="main-nav"><span>HOME</span><span>TECHNOLOGY</span><span>COMPANY</span><span>EVIDENCE</span><span>CONTACT</span></nav>
</header>

<section>
  <div class="hero-media" role="img" aria-label="Photo of a smiling doctor showing a phone to a patient resting in a hospital bed"></div>
  <h1 class="heading hero-title">Cost effective care<br>in oncology</h1>
  <a class="btn" style="left:172px;top:352px;width:258px;height:60px">Book an online appointment</a>
</section>

<section>
  <h2 class="heading about-title">About</h2>
  <p class="about-text">Tovane Medical, Inc. is an expert team with the vision of improving oncology treatment delivery, patient outcomes and cost effectiveness through the power of AI.</p>

  <div class="bubble" style="left:985px;top:803px;width:88px;height:88px"></div>
  <div class="bubble" style="left:1090px;top:905px;width:90px;height:90px"></div>
  <h2 class="heading section-title abs" style="left:172px;top:878px">The problem(s) for providers:</h2>
  <p class="body-copy abs" style="left:172px;top:937px;width:487px">creating a treatment directive starts from scratch for every patient and is a time consuming iterative/back and forth processFurther, because there is little transparency to communicate patient-specific treatment needs to the payer, prior authorization is a burden.</p>
  <a class="btn" style="left:172px;top:1067px;width:131px;height:61px">Read more</a>
  <div class="illus" role="img" aria-label="Illustration of a doctor inside a computer monitor with medical records and tablet" style="left:690px;top:840px;width:360px;height:278px;background:linear-gradient(160deg,#cfe9f8,#8cc9ef)"></div>

  <div class="bubble" style="left:141px;top:1172px;width:88px;height:88px"></div>
  <div class="bubble" style="left:34px;top:1277px;width:90px;height:90px"></div>
  <div class="illus" role="img" aria-label="Illustration of a female doctor with a clipboard on a computer screen among leaves" style="left:95px;top:1265px;width:388px;height:266px;background:linear-gradient(120deg,#3b8de0,#bfe2f7 55%,#f39a8a)"></div>
  <h2 class="heading section-title abs" style="left:541px;top:1283px">The problem(s) for payers:</h2>
  <p class="body-copy abs" style="left:541px;top:1341px;width:486px">The problem for payers: there is no transparency to the uniqueness of the patient so the process has costly delays to gather more information and align the treatment to what’s best for the patient; often attempts to redirect care are unfruitful.</p>
  <a class="btn" style="left:540px;top:1471px;width:131px;height:61px">Read more</a>
</section>

<section class="services">
  <h2 class="heading services-title">Our services</h2>

  <div class="service-icon" role="img" aria-label="Payer solution product icon" style="left:174px;top:175px"></div>
  <div class="service-name" style="left:317px;top:182px">Payer Solution</div>
  <p class="service-copy" style="left:318px;top:236px">until now, some improvements have been made in the digitization of prior authorization submissions. Tovane Medical AI is adding the automated intelligent decisioning.</p>

  <div class="service-icon" role="img" aria-label="Provider solution product icon" style="left:628px;top:175px"></div>
  <div class="service-name" style="left:771px;top:182px">Provider Solution</div>
  <p class="service-copy" style="left:772px;top:236px">until now, improvements have been made in the speed of computing time to arrive at a treatment directive after many days. Tovane Medical AI is adding the intelligent decisioning.</p>

  <div class="service-icon" role="img" aria-label="Innovation product icon" style="left:174px;top:380px"></div>
  <div class="service-name" style="left:317px;top:386px">Innovation</div>
  <p class="service-copy" style="left:318px;top:440px">Tovane Insight Artificial Intelligence (AI) decision support platform Clinically validated, FDA-cleared expert system with 30,000 patient treatment datasets.</p>

  <div class="service-icon" role="img" aria-label="Clinical evidence icon" style="left:628px;top:380px"></div>
  <div class="service-name" style="left:771px;top:386px">Clinical Evidence</div>
  <p class="service-copy" style="left:772px;top:440px">Quantifying temporal trends and the impact of advances in radiation planning on heart and lung dose for lung cancer treatment using a machine learning model.</p>
</section>

<section>
  <div class="bubble" style="left:985px;top:2328px;width:88px;height:88px"></div>
  <div class="bubble" style="left:1090px;top:2434px;width:90px;height:90px"></div>
  <h2 class="heading section-title abs" style="left:172px;top:2400px">Our vision</h2>
  <p class="body-copy abs" style="left:172px;top:2463px;width:487px;font-size:16px;line-height:30px">Tovane Medical, Inc. is an expert team with the vision of improving oncology treatment delivery, patient outcomes and cost effectiveness through the power of AI.</p>
  <a class="btn" style="left:172px;top:2593px;width:131px;height:60px">Read more</a>
  <div class="illus" role="img" aria-label="Illustration of a doctor stepping out of a computer screen holding a medical folder, with heart and plus speech bubbles" style="left:690px;top:2350px;width:366px;height:330px;border-radius:48% 52% 45% 55%;background:linear-gradient(150deg,#dff0fb,#a9d8f2)"></div>
</section>

<footer>
  <div class="contact-left">
    <div class="brand-name footer-brand">Tovane Medical</div>
    <h3 class="heading hours-title">Working hours</h3>
    <p class="hours" style="top:370px">Monday-Friday: 9am to 7pm</p>
    <p class="hours" style="top:415px">Saturday: 9am to 4pm</p>
    <p class="hours" style="top:460px">Sunday: Closed</p>
    <a class="btn" style="left:172px;top:515px;width:258px;height:60px;background:var(--sky-light);color:var(--brand)">Book an online appointment</a>
  </div>

  <div class="contact-right">
    <h3 class="heading form-title">For any questions contact<br>us here</h3>
    <span class="field-label" style="left:45px;top:203px">First Name</span>
    <span class="field-label" style="left:295px;top:203px">Last Name</span>
    <div class="field" style="left:46px;top:236px;width:229px;height:49px"></div>
    <div class="field" style="left:296px;top:236px;width:230px;height:49px"></div>
    <span class="field-label" style="left:45px;top:300px">Email*</span>
    <div class="field" style="left:46px;top:333px;width:480px;height:48px"></div>
    <span class="field-label" style="left:45px;top:405px">Add answer here</span>
    <div class="field" style="left:46px;top:436px;width:480px;height:99px;border-radius:40px"></div>
    <a class="btn" style="left:46px;top:560px;width:139px;height:46px;background:var(--brand);font-size:14px">Submit now</a>
  </div>

  <p class="copyright">Copyrights @ 2020 Tovane Medical. All Rights Reserved.</p>
</footer>

</body>
</html>
```